Wren Hollow Apartments
stationary
Wren Hollow Apartments - Real Estate
Creative Brief
Traditional
Tobias Lindqvist
2408 Wren Hollow Houston TX 77091
tjlindqvist@quellmail.example

```html
<!DOCTYPE html>
<html lang="en">
<head>
<meta charset="utf-8">
<title>Wren Hollow Apartments – Business Card</title>
<link rel="stylesheet" href="https://fonts.googleapis.com/css2?family=Marcellus&family=Crimson+Text:wght@400;600&display=swap">
<style>
  :root {
    --green: #2f8a3b;
    --green-dark: #25722f;
    --paper: #ffffff;
    --paper-shade: #f3f3f1;
    --ink: #2b2b2b;
    --backdrop: #dcdcdc;
  }
  * { box-sizing: border-box; margin: 0; padding: 0; }
  html, body { width: 1200px; height: 871px; overflow: hidden; }
  body {
    background: var(--backdrop);
    display: flex;
    flex-direction: column;
    align-items: center;
    justify-content: center;
    gap: 56px;
    font-family: "Crimson Text", Georgia, serif;
  }
  .card {
    width: 620px;
    height: 354px;
    position: relative;
    overflow: hidden;
    box-shadow: 0 6px 18px rgba(0,0,0,0.18);
  }

  /* Front */
  .card-front {
    background: var(--green);
    display: flex;
    flex-direction: column;
    align-items: center;
    justify-content: center;
    gap: 18px;
  }
  .brand-dot {
    width: 64px; height: 64px;
    border-radius: 50%;
    background: var(--paper);
  }
  .brand-name {
    font-family: "Marcellus", Georgia, serif;
    color: var(--paper);
    font-size: 34px;
    letter-spacing: 1px;
    text-align: center;
    line-height: 1.15;
  }

  /* Back */
  .card-back {
    background: var(--green);
  }
  .back-panel {
    position: absolute;
    left: 0; right: 0;
    top: 62px; bottom: 62px;
    background: linear-gradient(180deg, var(--paper) 0%, var(--paper-shade) 100%);
    border-top: 5px solid var(--paper);
    border-bottom: 5px solid var(--paper);
    outline: 2px solid var(--green-dark);
    outline-offset: -7px;
    display: flex;
    align-items: center;
  }
  .back-brand {
    width: 292px;
    display: flex;
    flex-direction: column;
    align-items: center;
    gap: 12px;
  }
  .back-brand .brand-dot { background: var(--green); width: 52px; height: 52px; }
  .back-brand .brand-name { color: var(--green); font-size: 24px; }
  .divider {
    width: 1px;
    height: 170px;
    background: #b9b9b9;
  }
  .contact {
    padding-left: 18px;
    color: var(--ink);
    font-size: 15px;
    line-height: 1.35;
  }
  .contact-name {
    font-family: "Marcellus", Georgia, serif;
    color: var(--green);
    font-size: 20px;
    letter-spacing: 0.5px;
    margin-bottom: 16px;
  }
  .contact-address { margin-bottom: 4px; }
  .contact-line { display: flex; align-items: center; gap: 7px; }
  .contact-line svg { width: 11px; height: 11px; fill: var(--green); flex: none; }
</style>
</head>
<body>
  <section class="card card-front" aria-label="Card front">
    <div class="brand-dot"></div>
    <div class="brand-name">Wren Hollow<br>Apartments</div>
  </section>

  <section class="card card-back" aria-label="Card back">
    <div class="back-panel">
      <div class="back-brand">
        <div class="brand-dot"></div>
        <div class="brand-name">Wren Hollow<br>Apartments</div>
      </div>
      <div class="divider"></div>
      <div class="contact">
        <p class="contact-name">Tobias Lindqvist</p>
        <p class="contact-address">2408 Wren Hollow<br>Houston TX 77091</p>
        <p class="contact-line">
          <svg viewBox="0 0 24 24" aria-hidden="true"><path d="M6.6 10.8a15.1 15.1 0 0 0 6.6 6.6l2.2-2.2a1 1 0 0 1 1-.25 11.4 11.4 0 0 0 3.6.57 1 1 0 0 1 1 1V20a1 1 0 0 1-1 1A17 17 0 0 1 3 4a1 1 0 0 1 1-1h3.5a1 1 0 0 1 1 1c0 1.25.2 2.45.57 3.57a1 1 0 0 1-.25 1z"/></svg>
          713-555-0182
        </p>
        <p class="contact-line">
          <svg viewBox="0 0 24 24" aria-hidden="true"><path d="M2 5h20v14H2z M4 7v.5l8 5 8-5V7l-8 5z" fill-rule="evenodd"/></svg>
          tjlindqvist@quellmail.example
        </p>
      </div>
    </div>
  </section>
</body>
</html>
```